We need a design for our security installation based business. Our name is K M Security Systems

We need a business card for a security installation based company. We want to look modern and professional. We would like our company logo used and the three main colours to be white, black and orange. We install intruder alarms, cctv and access control. Our preference would be to use the black/orange design on the front and orange/black on the back. Feel free to post variations.

Target Market(s)

Business owners, commercial property and large residential properties

Industry/Entity Type

Business

Contact Information for Business Card

Owen Pelham 07813 592 640

Liam Fenwick 07751 286 419

operations@kmsecuritysystems.co.uk

Intruder Alarms
CCTV
Access Control

Colors
f78f20
000000
ffffff

Requirements
Must have
• Must have the logo on the business card somewhere

```html
<!DOCTYPE html>
<html lang="en">
<head>
<meta charset="utf-8">
<title>K M Security Systems – Business Cards</title>
<link href="https://fonts.googleapis.com/css2?family=Lato:wght@400;700;900&display=swap" rel="stylesheet">
<style>
  :root {
    --orange: #ff4b0a;
    --black: #000000;
    --white: #ffffff;
    --stage: #3a3a3a;
    --ink: #1a1a1a;
  }
  * { box-sizing: border-box; margin: 0; padding: 0; }
  html, body {
    width: 1200px; height: 900px; overflow: hidden;
    background: var(--stage);
    font-family: "Lato", sans-serif;
  }
  .stage {
    width: 1200px; height: 900px;
    display: flex; align-items: center; justify-content: center; gap: 40px;
  }
  .card {
    position: relative;
    width: 540px; height: 350px;
    overflow: hidden;
    box-shadow: 0 10px 40px rgba(0,0,0,0.45);
  }
  /* Front card */
  .card-front { background: var(--white); }
  .card-front .swoosh { position: absolute; inset: 0; }
  .front-brand {
    position: absolute; left: 40px; top: 40px;
    display: flex; align-items: center; gap: 14px;
  }
  .brand-mark {
    width: 22px; height: 22px; background: var(--orange); flex: none;
  }
  .brand-name {
    font-weight: 900; font-size: 28px; letter-spacing: 0.5px;
    text-transform: uppercase; color: var(--black); line-height: 1.1;
  }
  .brand-name .line { display: block; }
  .contacts {
    position: absolute; left: 40px; top: 140px;
    display: flex; flex-direction: column; gap: 8px;
  }
  .contact-row { display: flex; align-items: center; gap: 10px; }
  .contact-name { color: var(--orange); font-weight: 700; font-size: 20px; min-width: 150px; }
  .contact-phone { color: var(--ink); font-size: 17px; display: flex; align-items: center; gap: 6px; }
  .contact-phone svg { width: 13px; height: 13px; }
  .contact-email {
    margin-top: 14px; color: var(--ink); font-size: 15px;
    display: flex; align-items: center; gap: 8px;
  }
  .contact-email svg { width: 14px; height: 11px; }
  /* Back card */
  .card-back {
    background: var(--black);
    display: flex; flex-direction: column; align-items: center; justify-content: center;
  }
  .back-brand .brand-name { color: var(--orange); font-size: 36px; text-align: center; }
  .back-rule { width: 360px; height: 4px; background: var(--orange); margin: 22px 0 20px; }
  .services { color: var(--white); font-size: 18px; letter-spacing: 0.3px; }
  .services .sep { color: var(--orange); margin: 0 6px; }
</style>
</head>
<body>
<main class="stage">
  <section class="card card-front" aria-label="Business card front">
    <svg class="swoosh" viewBox="0 0 540 350" preserveAspectRatio="none" aria-hidden="true">
      <path d="M330 0 Q470 120 450 350 L540 350 L540 0 Z" fill="var(--orange)"/>
      <path d="M345 0 Q482 120 462 350 L540 350 L540 0 Z" fill="var(--white)"/>
      <path d="M352 0 Q490 120 470 350 L540 350 L540 0 Z" fill="var(--black)"/>
    </svg>
    <div class="front-brand">
      <span class="brand-mark" aria-hidden="true"></span>
      <span class="brand-name"><span class="line">K M Security</span><span class="line">Systems</span></span>
    </div>
    <div class="contacts">
      <div class="contact-row">
        <span class="contact-name">Owen Pelham</span>
        <span class="contact-phone">
          <svg viewBox="0 0 24 24" aria-hidden="true"><path fill="var(--orange)" d="M6.6 10.8a15.1 15.1 0 0 0 6.6 6.6l2.2-2.2a1 1 0 0 1 1-.25 11.4 11.4 0 0 0 3.6.57 1 1 0 0 1 1 1V20a1 1 0 0 1-1 1A17 17 0 0 1 3 4a1 1 0 0 1 1-1h3.5a1 1 0 0 1 1 1c0 1.25.2 2.45.57 3.57a1 1 0 0 1-.25 1z"/></svg>
          07813 592 640
        </span>
      </div>
      <div class="contact-row">
        <span class="contact-name">Liam Fenwick</span>
        <span class="contact-phone">
          <svg viewBox="0 0 24 24" aria-hidden="true"><path fill="var(--orange)" d="M6.6 10.8a15.1 15.1 0 0 0 6.6 6.6l2.2-2.2a1 1 0 0 1 1-.25 11.4 11.4 0 0 0 3.6.57 1 1 0 0 1 1 1V20a1 1 0 0 1-1 1A17 17 0 0 1 3 4a1 1 0 0 1 1-1h3.5a1 1 0 0 1 1 1c0 1.25.2 2.45.57 3.57a1 1 0 0 1-.25 1z"/></svg>
          07751 286 419
        </span>
      </div>
      <div class="contact-email">
        <svg viewBox="0 0 14 11" aria-hidden="true"><rect width="14" height="11" fill="var(--orange)"/><path d="M0 0 L7 6 L14 0" stroke="var(--white)" stroke-width="1.4" fill="none"/></svg>
        operations@kmsecuritysystems.co.uk
      </div>
    </div>
  </section>

  <section class="card card-back" aria-label="Business card back">
    <div class="back-brand">
      <span class="brand-name">K M Security Systems</span>
    </div>
    <div class="back-rule" aria-hidden="true"></div>
    <p class="services">Intruder Alarms<span class="sep">|</span>CCTV<span class="sep">|</span>Access Control</p>
  </section>
</main>
</body>
</html>
```